Packaging Design Project

PLEASE NOTE: YOU MUST USE ADOBE ILLUSTRATOR FOR THIS PROJECT.
I need a design for a plastic bag packaging for our product, Verminox. Please see the website for more information about the product we sell, www.harvest-pure-living.example
Colours to use are red, green and yellow of various tones and shades.
The dimensions of the bag are approximately: 20cm wide by 25cm high with a 3.5 to 4 cm side width.
Front of Bag
Must have the company logo – please see attached file A1 Q.pdf. Please separate this label in two. i.e. the company logo is only the part that says Harvest Pure Living (with the green heartbeat design)
Also must have the product logo/signage – see the file A1 Q.pdf (attached). Please delete the Pty Ltd after the company name.
Must have product information: according to these words: “easy to use, safe around pets and children, non toxic, no chemicals”
The upper top of the bag must have the words: “resealable pack: cut here to start your cleaner, kinder future.”
The front of the bag also must have a picture relating to the product - plant and/or animal picture. Please see the website for more ideas of what pictures you can include. www.harvest-pure-living.example. The picture must be large and take up most of the front of the bag. It must be eye catching, being the first thing the customers see.
Must have the following words somewhere on the front of the bag
• No more pests
• No more chemicals
• No more worries
• Pet friendly
Also must include: “Controls fleas, flea larvae and flea eggs: bedbugs: lice and mites: flies and biting flies: hookworm, roundworm and tapeworms”
Front must also include: KTR certification, Product of Australia, Cape Renwick company logo, approximately 2 x 2 cm
Front, back and sides of bag should have the quantity amount
Sides of bag must have company name and product name
Back of bag
Must have 1 small paragraph about the company. See attached file Company Background.doc
1 small paragraph about congratulating customer for buying a clean safe effective product.- this has to be the dominant feature of the back of the bag. It must be large and eye catching
1 paragraph about Verminox and how it works. – also included in the file Company Background.doc.
Must have an analysis of what's in the product – please see attached file
Must include rates of application – please see attached file Rates of Application.doc
Back of bag must include company logo somewhere – leave space for this
must include safety directions and barcode –please see attached file Safety Directions.doc
Forgot to tell you all that the design has to be done in Adobe Illustrator Version 10 and above. Thanks!
Reason: Hi Everyone
The project has been extended by 2 days. Keep all those designs coming in!
Hi Designers,
Here is an update to the brief which I think will make your lives easier!
Update/Changes
The dimensions of the bag are confirmed to be 21cm wide by 29cm high.
Please delete the previous information and change it to the following:
Controls fleas, bedbugs, lice, mites, flies, biting flies, hookworm, roundworm and tapeworm in pets.
Controls aphids, mealy bugs, harlequin bugs, white fly and cabbage aphids on plants.
Please put the following words under the product label, under the word "Verminox":
Active Constituents:900g/kg amorphous silica
The safety directions has changed. It should now read:
Safety Directions
May irritate eyes and skin. Avoid contact with eyes and skin. Do not inhale dust. Wash hands after use.
Please note:
In the file we uploaded, the Verminox label had a heartbeat line which ended with "Harvest Pure Living....etc. Somehow everyone has lost this beepy line. Please put back the beepy line on
the Verminox word.

```html
<!DOCTYPE html>
<html lang="en">
<head>
<meta charset="utf-8">
<title>Verminox pouch – front and back</title>
<link rel="stylesheet" href="https://fonts.googleapis.com/css2?family=Oswald:wght@500;700&family=Open+Sans:wght@400;600;700&display=swap">
<style>
:root{
  --bg:#ececec;
  --white:#ffffff;
  --green:#5a9a1c;
  --green-light:#8cc63f;
  --green-dark:#2f6b12;
  --brown:#2b1a12;
  --ink:#4a4a4a;
  --yellow:#f5c400;
  --red:#d42a1e;
  --plant:#6fae2e;
}
*{box-sizing:border-box;margin:0;padding:0}
html,body{width:1200px;height:1018px;overflow:hidden;background:var(--bg)}
body{font-family:"Open Sans",Arial,sans-serif;color:var(--ink);position:relative}
.panel{position:absolute;top:50px;width:520px;height:920px;background:var(--white);overflow:hidden;box-shadow:0 6px 18px rgba(0,0,0,.12)}
.panel--front{left:50px}
.panel--back{left:630px}
.abs{position:absolute}

/* front */
.cut-line{left:0;right:0;top:150px;border-top:2px dashed var(--green-light)}
.scissors{right:30px;top:132px}
.reseal-note{right:24px;top:160px;text-align:right;font-size:13px;line-height:1.3;color:var(--green);font-weight:600}
.brand{display:flex;align-items:center;gap:8px}
.brand__dot{width:16px;height:16px;border-radius:50%;background:var(--green-light)}
.brand__name{font-family:"Open Sans",Arial,sans-serif;font-weight:700;color:var(--green-dark);font-size:20px}
.brand--front{left:30px;top:235px}
.product-name{left:24px;top:272px;font-family:"Oswald",Arial,sans-serif;font-weight:700;font-size:96px;line-height:1;color:var(--green);letter-spacing:1px}
.constituents{left:24px;top:392px;width:410px;height:30px;background:var(--green-dark);color:var(--white);font-size:16px;font-weight:600;line-height:30px;padding-left:12px}
.claims{left:30px;width:268px;font-size:16px;line-height:1.35;color:var(--ink)}
.claims--pets{top:460px}
.claims--plants{top:565px}
.promise-box{left:305px;top:610px;width:200px;height:100px;background:var(--green-light);color:var(--white);font-size:12px;font-weight:700;line-height:1.35;padding:14px 12px}
.features{left:305px;top:718px;width:200px;font-size:12px;line-height:1.35;color:var(--green)}
.plant-art{border-radius:40% 40% 10% 10%;background:linear-gradient(180deg,#b7dd7d,var(--plant))}
.plant-art--front{left:410px;top:436px;width:70px;height:164px}
.animal-art{left:30px;top:700px;width:260px;height:140px;background:linear-gradient(180deg,#5a4033,var(--brown));border-radius:30% 30% 0 0}
.soil-band{left:0;right:0;bottom:0;height:90px;background:var(--brown)}
.cert-mark{width:48px;height:48px;background:#f2f2f2;border-radius:4px}
.cert-mark--one{left:30px;bottom:22px}
.cert-mark--two{left:90px;bottom:22px;background:var(--yellow)}
.organic-seal{right:130px;bottom:18px;width:96px;height:96px;border-radius:50%;background:var(--green-light);border:4px solid var(--white)}

/* back */
.brand--back{left:24px;top:88px}
.brand--back .brand__name{font-size:16px}
.about{left:24px;top:130px;width:270px;font-size:9px;line-height:1.4;color:var(--ink)}
.about p+p{margin-top:8px}
.about h3{font-size:9px;font-weight:700;margin-top:8px}
.analysis{left:305px;top:120px;width:195px;border:1.5px solid var(--green-light);border-radius:6px;overflow:hidden}
.analysis__title{background:var(--green-light);color:var(--white);font-size:10px;font-weight:700;padding:4px 8px}
.analysis__intro{font-size:8px;padding:5px 8px 2px;font-weight:600}
.analysis table{width:100%;border-collapse:collapse;font-size:7.5px;margin:0 0 6px}
.analysis td{padding:1px 8px}
.analysis td+td{text-align:right}
.congrats{left:14px;top:432px;width:492px;background:var(--green-light);color:var(--white);padding:8px 12px;border-radius:4px}
.congrats h2{font-family:"Oswald",Arial,sans-serif;font-weight:500;font-size:14px;color:#eaffc8}
.congrats p{font-size:9.5px;line-height:1.35}
.rates{left:24px;top:524px;width:300px;border:2px solid var(--yellow);border-radius:6px;background:var(--white);overflow:hidden}
.rates__title{background:var(--yellow);color:var(--white);font-size:11px;font-weight:700;padding:4px 10px}
.rate{display:flex;gap:6px;padding:4px 8px;border-bottom:1px solid #eee;font-size:7.5px;line-height:1.35}
.rate:last-child{border-bottom:0}
.rate__body{flex:1}
.rate__body b{display:block;color:var(--green);font-size:8px}
.rate__icon{width:16px;height:16px;background:#3a2a20;border-radius:3px;align-self:center}
.plant-art--back{left:400px;top:540px;width:90px;height:250px}
.soil-band--back{height:110px}
.safety{right:20px;bottom:62px;width:150px;font-size:8px;line-height:1.3;color:var(--red)}
.safety b{display:block}
.contact{right:20px;bottom:10px;width:150px;font-size:7px;line-height:1.35;color:var(--white)}
</style>
</head>
<body>

<section class="panel panel--front" aria-label="Pouch front">
  <div class="abs cut-line"></div>
  <svg class="abs scissors" width="34" height="34" viewBox="0 0 34 34" aria-hidden="true">
    <circle cx="8" cy="8" r="5" fill="none" stroke="#5a9a1c" stroke-width="2.5"/>
    <circle cx="8" cy="26" r="5" fill="none" stroke="#5a9a1c" stroke-width="2.5"/>
    <line x1="12" y1="11" x2="32" y2="24" stroke="#5a9a1c" stroke-width="2.5"/>
    <line x1="12" y1="23" x2="32" y2="10" stroke="#5a9a1c" stroke-width="2.5"/>
  </svg>
  <p class="abs reseal-note">resealable pack:<br>cut here to start your cleaner, kinder future</p>

  <div class="abs brand brand--front"><span class="brand__dot"></span><span class="brand__name">Harvest Pure Living</span></div>
  <h1 class="abs product-name">VERMINOX</h1>
  <div class="abs constituents">Active Constituents:900g/kg amorphous silica</div>

  <div class="abs plant-art plant-art--front" role="img" aria-label="Climbing green plant with round leaves"></div>

  <p class="abs claims claims--pets">Controls fleas, bedbugs, lice, mites, flies, biting flies, hookworm, roundworm and tapeworm in pets.</p>
  <p class="abs claims claims--plants">Controls aphids, mealy bugs, harlequin bugs, white fly and cabbage aphids on plants</p>

  <div class="abs promise-box">NO MORE PESTS<br>NO MORE CHEMICALS<br>NO MORE WORRIES<br>PET FRIENDLY</div>
  <p class="abs features">easy to use, safe around pets and children, non toxic, no chemicals</p>

  <div class="abs animal-art" role="img" aria-label="Silhouettes of a hen and a dog"></div>
  <div class="abs soil-band"></div>
  <div class="abs cert-mark cert-mark--one" role="img" aria-label="Certification badge"></div>
  <div class="abs cert-mark cert-mark--two" role="img" aria-label="Product of Australia badge"></div>
  <div class="abs organic-seal" role="img" aria-label="100% organic seal"></div>
</section>

<section class="panel panel--back" aria-label="Pouch back">
  <div class="abs brand brand--back"><span class="brand__dot"></span><span class="brand__name">Harvest Pure Living</span></div>

  <div class="abs about">
    <p>Harvest Pure Living is an Australian company and also the first company in Australia to supply Verminox as a means of controlling insects and pests on plants, vegetables and animals. We are a company committed to finding organic ways for you to live a greener, longer, happier life, not just in the house, and but also in industry and farming.</p>
    <h3>Verminox</h3>
    <p>This is our insecticide product. A natural product registered with the National Agri-Chemicals Authority for use against insect pests of stored grain and registered as an allowable input for organic farmers by the KTR. Verminox kills insects by absorbing oils and waxes from the insect cuticle thus facilitating moisture loss and death by dehydration.</p>
  </div>

  <div class="abs analysis">
    <div class="analysis__title">VERMINOX MINERAL ANALYSIS</div>
    <p class="analysis__intro">Harvest Pure Living Verminox contains these minerals:</p>
    <table>
      <tr><td>Silicon Dioxide (SiO2)</td><td>90.10%</td></tr>
      <tr><td>Phosphorus Pentoxide (P2O5)</td><td>0.03%</td></tr>
      <tr><td>Aluminium Oxide (Al2O3)</td><td>4.62%</td></tr>
      <tr><td>Titanium Dioxide (TiO2)</td><td>0.37%</td></tr>
      <tr><td>Iron Oxide (Fe2O3)</td><td>3.16%</td></tr>
      <tr><td>Vanadium Oxide (V2O5)</td><td>0.03%</td></tr>
      <tr><td>Manganese Oxide (MnO)</td><td>0.02%</td></tr>
      <tr><td>Chromium Oxide (Cr2O3)</td><td>0.005%</td></tr>
      <tr><td>Magnesium Oxide (MgO)</td><td>0.56%</td></tr>
      <tr><td>Copper Oxide (CuO)</td><td>0.004%</td></tr>
      <tr><td>Calcium Oxide (CaO)</td><td>0.62%</td></tr>
      <tr><td>Zinc Oxide (ZnO)</td><td>0.007%</td></tr>
      <tr><td>Sodium Oxide (Na2O)</td><td>0.11%</td></tr>
      <tr><td>Potassium Oxide (K2O)</td><td>0.06%</td></tr>
      <tr><td>Sulphur Trioxide (SO3)</td><td>0.06%</td></tr>
      <tr><td>Chlorine (Cl)</td><td>0.05%</td></tr>
    </table>
  </div>

  <div class="abs congrats">
    <h2>CONGRATULATIONS</h2>
    <p>Congratulations on your purchase of Verminox! You have selected an exceptional product with superior performance. You should be proud of purchasing a product that is certified organic and beneficial to the environment and leaving your carbon footprint on this planet.</p>
  </div>

  <div class="abs plant-art plant-art--back" role="img" aria-label="Young green plant sprouting from soil"></div>

  <div class="abs rates">
    <div class="rates__title">RATES OF APPLICATION</div>
    <div class="rate"><div class="rate__body"><b>Poultry</b>0-8 weeks: use 30g Verminox to 5kg feed, 3 times a week. 8-16 weeks: use 30g Verminox per kg of feed.</div><span class="rate__icon" role="img" aria-label="Hen icon"></span></div>
    <div class="rate"><div class="rate__body"><b>Rabbits, Guinea Pigs and Small Animals</b>Add 1 teaspoon Verminox per serving of grain feed. Apply monthly.</div><span class="rate__icon" role="img" aria-label="Rabbit icon"></span></div>
    <div class="rate"><div class="rate__body"><b>Garden</b>To apply Verminox, use any dusting equipment. When spraying, apply Verminox to upper and lower leaf surfaces to obtain the best results. When treating grain, use 80g per 1 litre of water.</div><span class="rate__icon" role="img" aria-label="Leaf icon"></span></div>
    <div class="rate"><div class="rate__body"><b>Dogs and Cats</b>When applying to dry pet feeds, the following are suggested rates per day: Kittens ¼ teaspoon; Cats 1 teaspoon; Puppies ½ to 1 teaspoon; Dogs under 16kg 1 teaspoon; Dogs over 45kg 2 tablespoons.</div><span class="rate__icon" role="img" aria-label="Dog and cat icon"></span></div>
    <div class="rate"><div class="rate__body"><b>Birds</b>Dust Verminox between feathers of birds, repeating where necessary.</div><span class="rate__icon" role="img" aria-label="Bird icon"></span></div>
    <div class="rate"><div class="rate__body"><b>Bedbugs</b>Dust Verminox on each leg of bed. Also, dust Verminox onto seams and bedding and especially on any crevices of the bedding.</div><span class="rate__icon" role="img" aria-label="Bedbug icon"></span></div>
  </div>

  <div class="abs soil-band soil-band--back"></div>
  <p class="abs safety"><b>SAFETY DIRECTIONS</b>May irritate eyes and skin. Avoid contact with eyes and skin. Do not inhale dust. Wash hands after use.</p>
  <p class="abs contact">12 Larkspur Lane, Cape Renwick QLD 4999<br>PH 0400 000 123<br>FAX (07) 5550 0144<br>www.harvest-pure-living.example</p>
</section>

</body>
</html>
```